Pepper's Parlor New Packaging Design for Award Winning Dog Treats available on store shelves!

Pepper's Parlor Pup Snack Bakehouse specializes in baking healthy all natural dog treats using local farm produce from Mississippi. We have 3 flavors of treats and this project would include 3 variations of the same design designated by color and flavor. The box has already been designed and our current labels have been added to box for a starting point. But this needs to be expanded upon and made into a stellar eye catching product for store shelves. Currently, each flavor is designated by a different color ribbon and flavor label. I would like for there to be a bow tie at the top of the box with the color pattern designation per flavor. Our current packaging is simple but has a certain down home country southern appeal. I want to keep that. The words to think about when designing are farm fresh produce, healthy, all natural, farm to dog bowl. We may need to add a picture of me and Pepper and that can be supplied. Green color is set, dark brown color is set. Really want to use the color patterns for the flavors that are already used. I want the background of design to be a burlap bag print. The new design of the box needs to be similar to the current bag design. There needs to be a subtle but better change to the new packaging as we are already on stores shelves and will hopefully national by the end of next year.
Updates

Project Deadline Extended Reason: Design needs to be similar to original design because it is already on store shelves but should meet all design requests for new packaging. Box design pdf is what you will be working from. Final design should be in a working PDF format. Added Wednesday, December 30, 2015

Industry/Entity Type

Cafe

Font styles to use
Other font styles liked:
• Gigi

Colors
abd037
add136
cadf83
ffffff
9bcb3c

Requirements
Must have
• Must design the box shape that is predetermined in the attached PDF
• Must include current fonts
• Must look as similar to current design as possible
• Must include current colors
• PLEASE DESIGN ENTIRE PRODUCT (refer to box design PDF)

```html
<!DOCTYPE html>
<html lang="en">
<head>
<meta charset="utf-8">
<title>Pepper's Parlor – Blueberry Honey Box Dieline</title>
<link href="https://fonts.googleapis.com/css2?family=Marcellus&family=Roboto+Condensed:wght@400;700&family=Kalam:wght@400&display=swap" rel="stylesheet">
<style>
  :root{
    --kraft:#ab8c68;
    --green:#add136;
    --green-light:#cadf83;
    --brown:#3b2418;
    --dim-blue:#2f9fd8;
    --fold-red:#d8332b;
    --white:#ffffff;
    --ink:#2a1a10;
  }
  *{box-sizing:border-box;margin:0;padding:0}
  html,body{width:1200px;height:875px;overflow:hidden;background:#ffffff}
  .canvas{position:relative;width:1200px;height:875px;font-family:"Roboto Condensed",sans-serif;color:var(--ink)}
  .dieline{position:absolute;inset:0}
  .dim-label{position:absolute;font-family:"Roboto Condensed",sans-serif;font-size:17px;color:var(--dim-blue)}
  .dim-label.small{font-size:14px}

  .flavor-card{position:absolute;left:154px;top:342px;width:106px;height:390px;background:var(--green);border:2px solid var(--white);border-radius:10px;padding:8px 6px;text-align:center}
  .flavor-card .card-tag{font-family:"Marcellus",serif;font-size:8px;color:var(--brown);letter-spacing:.5px}
  .flavor-card .card-name{font-family:"Marcellus",serif;font-size:17px;color:var(--brown);line-height:1.05;margin:6px 0}
  .flavor-card .card-sub{font-family:"Marcellus",serif;font-size:7px;color:var(--brown);border-top:1px solid var(--brown);border-bottom:1px solid var(--brown);padding:1px 0;margin-bottom:6px}
  .flavor-card .flavor-name{position:absolute;left:6px;bottom:10px;width:52px;background:var(--green-light);border:1px solid var(--white);border-radius:4px;font-family:"Kalam",cursive;font-size:11px;line-height:1;padding:4px 2px;color:var(--brown)}
  .story{position:absolute;left:266px;top:350px;width:162px;font-size:8.2px;line-height:1.28;color:var(--ink)}
  .story h3{font-size:11px;font-weight:700;letter-spacing:.3px;margin-bottom:1px}
  .story p{margin-bottom:3px}
  .story .support{font-size:7.5px}
  .tagline-script{position:absolute;left:266px;top:602px;width:106px;font-family:"Kalam",cursive;font-size:10px;line-height:1.1;color:#5b7b1a}
  .maker{position:absolute;left:266px;top:630px;font-size:6.5px;line-height:1.2}
  .badge-seal{position:absolute;left:376px;top:598px;width:42px;height:42px;border-radius:50%;background:var(--green-light);border:2px solid var(--brown)}
  .ingredients{position:absolute;left:266px;top:658px;width:162px;border:1px solid var(--ink);padding:2px 3px;font-size:5.8px;line-height:1.2}
  .nutrition{position:absolute;left:154px;top:737px;width:274px;border-top:1px solid var(--ink);border-bottom:1px solid var(--ink);font-size:5.3px;padding:1px 0;letter-spacing:.2px}
  .socials{position:absolute;left:154px;top:752px;width:274px;display:flex;justify-content:space-between;font-size:7.5px}
  .socials span::before{content:"";display:inline-block;width:7px;height:7px;background:var(--ink);margin-right:2px;vertical-align:-1px}
  .site{position:absolute;left:154px;top:765px;width:274px;text-align:center;font-size:8px}

  .ribbon{position:absolute;top:154px;height:632px;background:linear-gradient(90deg,#4a2e1f 0%,#7a9a2c 30%,#3d2519 55%,#9bbf3c 80%,#4a2e1f 100%);opacity:.95}

  .front-label{position:absolute;left:637px;top:333px;width:224px;height:414px}
  .front-label svg{position:absolute;inset:0}
  .brand-name{position:absolute;left:0;right:0;top:30px;text-align:center;font-family:"Marcellus",serif;font-size:30px;line-height:1;color:var(--brown)}
  .award{position:absolute;top:148px;font-family:"Roboto Condensed",sans-serif;font-size:13px;color:var(--white)}
  .award.left{left:20px}.award.right{right:14px}
  .pet-portrait{position:absolute;left:72px;top:124px;width:80px;height:80px;border-radius:50%;background:radial-gradient(circle at 50% 40%,#e9e2d6,#8c7a66);border:3px solid var(--white)}
  .product-line{position:absolute;left:0;right:0;top:318px;text-align:center;font-family:"Marcellus",serif;color:var(--white);line-height:1.05}
  .product-line .l1,.product-line .l2{font-size:27px}
  .product-line .l2{letter-spacing:1px}
  .values{position:absolute;left:585px;top:760px;width:307px;text-align:center;font-family:"Marcellus",serif;font-size:13.5px;color:var(--brown);letter-spacing:.5px}
</style>
</head>
<body>
<div class="canvas">

  <svg class="dieline" width="1200" height="875" viewBox="0 0 1200 875" aria-hidden="true">
    <g fill="var(--kraft)" stroke="#222" stroke-width="1">
      <path d="M81 178 L127 154 L127 786 L81 762 Z"/>
      <path d="M127 154 L434 154 L434 302 L127 302 Z"/>
      <path d="M434 176 L450 154 L585 154 L585 302 L434 302 Z"/>
      <path d="M585 154 L620 154 L620 72 L655 72 L670 92 L805 92 L820 72 L857 72 L857 154 L892 154 L892 302 L585 302 Z"/>
      <path d="M892 154 L1025 154 L1040 176 L1040 302 L892 302 Z"/>
      <rect x="127" y="302" width="913" height="484"/>
      <path d="M127 786 L170 786 L200 836 L260 836 L290 866 L400 866 L434 826 L434 786 Z"/>
      <path d="M434 786 L585 786 L585 826 L555 866 L470 866 L434 836 Z"/>
      <path d="M585 786 L892 786 L892 826 L850 866 L640 866 L612 836 L585 836 Z"/>
      <path d="M892 786 L1040 786 L1040 836 L1010 866 L930 866 L892 826 Z"/>
    </g>
    <path d="M243 206 Q275 196 308 206 L308 212 Q275 202 243 212 Z" fill="#fff" stroke="#222"/>
    <g stroke="var(--fold-red)" stroke-width="1" stroke-dasharray="4 3" fill="none">
      <line x1="127" y1="302" x2="1040" y2="302"/>
      <line x1="127" y1="786" x2="1040" y2="786"/>
      <line x1="127" y1="154" x2="127" y2="786"/>
      <line x1="434" y1="154" x2="434" y2="866"/>
      <line x1="585" y1="154" x2="585" y2="866"/>
      <line x1="892" y1="154" x2="892" y2="866"/>
      <line x1="620" y1="154" x2="857" y2="154"/>
    </g>
    <g stroke="var(--dim-blue)" stroke-width="1" fill="none">
      <line x1="81" y1="20" x2="1180" y2="20"/>
      <line x1="81" y1="56" x2="1040" y2="56"/>
      <line x1="81" y1="12" x2="81" y2="100"/><line x1="127" y1="48" x2="127" y2="100"/>
      <line x1="434" y1="48" x2="434" y2="100"/><line x1="585" y1="48" x2="585" y2="100"/>
      <line x1="892" y1="48" x2="892" y2="100"/><line x1="1040" y1="48" x2="1040" y2="100"/>
      <line x1="1180" y1="12" x2="1180" y2="40"/>
      <line x1="30" y1="154" x2="30" y2="866"/>
      <line x1="20" y1="154" x2="81" y2="154"/><line x1="20" y1="302" x2="127" y2="302"/>
      <line x1="20" y1="786" x2="127" y2="786"/><line x1="20" y1="866" x2="127" y2="866"/>
      <line x1="1100" y1="72" x2="1100" y2="786"/>
      <line x1="1150" y1="154" x2="1150" y2="866"/>
      <line x1="857" y1="72" x2="1110" y2="72"/><line x1="1040" y1="154" x2="1160" y2="154"/>
      <line x1="1040" y1="302" x2="1110" y2="302"/><line x1="1040" y1="786" x2="1110" y2="786"/>
      <line x1="1040" y1="866" x2="1160" y2="866"/>
    </g>
  </svg>

  <span class="dim-label" style="left:584px;top:0">14<sup>11</sup>⁄<sub>32</sub></span>
  <span class="dim-label small" style="left:96px;top:36px">5⁄8</span>
  <span class="dim-label" style="left:262px;top:34px">4 5⁄8</span>
  <span class="dim-label" style="left:490px;top:34px">2 1⁄4</span>
  <span class="dim-label" style="left:720px;top:34px">4 5⁄8</span>
  <span class="dim-label" style="left:946px;top:34px">2 7⁄32</span>
  <span class="dim-label small" style="left:1066px;top:100px">1 1⁄4</span>
  <span class="dim-label" style="left:1052px;top:216px">2.35</span>
  <span class="dim-label" style="left:1154px;top:498px">12.225</span>
  <span class="dim-label" style="left:1094px;top:528px">7</span>
  <span class="dim-label" style="left:1060px;top:818px">1 5⁄8</span>
  <span class="dim-label" style="left:2px;top:218px">2.257</span>
  <span class="dim-label" style="left:22px;top:528px">7</span>
  <span class="dim-label" style="left:26px;top:816px">1 5⁄8</span>

  <div class="ribbon" style="left:434px;width:151px" role="img" aria-label="Brown, green and white plaid ribbon pattern for the Blueberry Honey flavor"></div>
  <div class="ribbon" style="left:892px;width:148px" role="img" aria-label="Brown, green and white plaid ribbon pattern for the Blueberry Honey flavor"></div>

  <div class="flavor-card">
    <div class="card-tag">PUP SNACK BAKEHOUSE</div>
    <div class="card-name">Pepper's Parlor</div>
    <div class="card-sub">FARM TO PUP BOWL</div>
    <div class="flavor-name">Blueberry Honey</div>
  </div>
  <div class="story">
    <h3>OUR STORY:</h3>
    <p>When June Whitaker rescued a little one pound dog named Pepper, she quickly found out this was the start of something special. Pepper, a boxer-pointer mix, made great progress in her first few months with June. But, despite her healthy growth, Pepper continued to experience some health issues. June, always resourceful, started creating her own solutions to treat Pepper's ailments by testing a theory that local honey could help Pepper's allergies, the same way it did for humans. June made dog treats from local farm produce, including honey, and no artificial ingredients. As June's love for Pepper grew, so did an idea. Why shouldn't all dogs have the benefits of Farm to Pup Bowl treats? From that experiment of love, Pepper's Parlor Pup Snack Bakehouse was born. And Pepper, once a little one pound rescue, is now a 70 pound tail waggin' mess!</p>
    <p class="support">Proud Supporter of the Riverbend County Humane Society. ADOPT A DOG TODAY! www.pepperspups.example</p>
  </div>
  <div class="tagline-script">Baked with love,<br>made for happy tails!</div>
  <div class="badge-seal" role="img" aria-label="Partner seal"></div>
  <div class="maker">MANUFACTURED AND DISTRIBUTED BY:<br>PEPPER'S PARLOR LLC, MILLBROOK MS 38601</div>
  <div class="ingredients">UNBLEACHED WHEAT FLOUR, NATURAL WHOLE GRAIN OATS, WATER, LOCAL BLUEBERRIES, NATURAL PEANUT BUTTER, APPLE CIDER VINEGAR, LOCAL HONEY, PARSLEY, BAKING POWDER<br><b>ALLERGEN INFORMATION:</b> MADE WITH PEANUTS AND WHEAT</div>
  <div class="nutrition">GUARANTEED ANALYSIS: PROTEIN 11% MIN · FAT 5% MIN · FIBER 3% MAX · MOISTURE 10% MAX · NET WT 8 OZ</div>
  <div class="socials"><span>Facebook.com/PeppersParlor</span><span>@PeppersParlor</span><span>@PeppersParlor</span></div>
  <div class="site">www.PeppersParlor.example</div>

  <div class="front-label">
    <svg width="224" height="414" viewBox="0 0 224 414" aria-hidden="true">
      <path d="M6 408 L6 60 Q112 -14 218 60 L218 408 Z" fill="var(--green)" stroke="var(--white)" stroke-width="4"/>
      <rect x="6" y="150" width="212" height="34" fill="var(--brown)" opacity=".85"/>
      <line x1="14" y1="300" x2="210" y2="300" stroke="var(--white)" stroke-width="2"/>
    </svg>
    <div class="brand-name">Pepper's<br>Parlor</div>
    <div class="award left">Award</div>
    <div class="award right">Winning</div>
    <div class="pet-portrait" role="img" aria-label="Round portrait photo of Pepper the dog"></div>
    <div class="product-line"><div class="l1">PUP SNACK</div><div class="l2">BAKEHOUSE</div></div>
  </div>
  <div class="values">WHOLESOME·SIMPLE·HOMEGROWN·WAG</div>

</div>
</body>
</html>
```